Flyer for the Harvest of lanterns conference

Flyer design for an annual international conference called "MERIVAL 2017". This is a conference for young adults, so we hope to produce a design that is both professional and appealing to young people in general

We'd like the flyer to showcase the conference brand logo, and clearly highlight the key information to people who will read it.

Target Market(s)

Young people, young adults

Industry/Entity Type

Religious

Font styles to use
Sans Serif

Colors

Designer to choose colors to be used in the design.

Requirements
Must have
• - Should be only one page (Vertical or Horizontal).
• - the MERVAL logo and all the information found in the attached text file. This includes: Main topic: Your sons and daughters shall prophesy,
• Dates and time, location, contact information and everything that is in the attached text file.
Nice to have
• It would be nice to see samples where the white logo is used and another where the black one is used.
Should not have
• This is NOT a folded flyer, we will be sticking it on doors and public places. And we will be printing large simple to put on walls. So only one page with few words like an add (the words are in the attached file)

```html
<!DOCTYPE html>
<html lang="en">
<head>
<meta charset="utf-8">
<title>MERIVAL 2017 – Harvest of lanterns conference</title>
<link href="https://fonts.googleapis.com/css2?family=Lato:wght@400;700&family=Oswald:wght@500;700&display=swap" rel="stylesheet">
<style>
  :root {
    --orange: #f0780f;
    --orange-deep: #e5620a;
    --ink: #2b2b2b;
    --grey-text: #555555;
    --grey-avatar: #9a9a9a;
    --panel: #f3f3f3;
    --bg: #e9e6e2;
    --white: #ffffff;
  }
  * { box-sizing: border-box; margin: 0; padding: 0; }
  html, body { width: 1200px; height: 1200px; overflow: hidden; background: var(--bg); }
  .flyer {
    position: absolute; left: 205px; top: 41px;
    width: 940px; height: 1330px;
    transform: scale(0.84); transform-origin: top left;
    background: var(--white); overflow: hidden;
    font-family: "Lato", sans-serif; color: var(--ink);
    box-shadow: 0 6px 24px rgba(0,0,0,.18);
  }
  .shapes { position: absolute; inset: 0; }
  .brand { position: absolute; left: 38px; top: 28px; width: 200px; text-align: center; }
  .brand-dot { display: block; width: 110px; height: 110px; margin: 0 auto 12px; border-radius: 50%; background: var(--orange); }
  .brand-name { font-size: 36px; font-weight: 700; letter-spacing: 2px; color: var(--ink); }
  .headline {
    position: absolute; left: 90px; top: 560px; width: 780px;
    transform: rotate(-15deg); transform-origin: center;
    text-align: center; color: var(--white); white-space: nowrap;
  }
  .headline-title { font-family: "Oswald", sans-serif; font-weight: 700; font-size: 90px; line-height: 1; letter-spacing: 1px; }
  .headline-sub { font-size: 44px; font-weight: 700; line-height: 1.1; margin-top: 4px; }
  .theme {
    position: absolute; left: 535px; top: 780px;
    font-family: "Oswald", sans-serif; font-weight: 500; font-size: 33px;
    line-height: 54px; color: var(--grey-text); letter-spacing: -0.2px;
    white-space: nowrap;
  }
  .speakers { position: absolute; left: 33px; top: 862px; }
  .speakers-title { font-size: 32px; font-weight: 400; color: var(--ink); margin-bottom: 18px; }
  .speaker { display: flex; align-items: center; height: 74.5px; }
  .speaker-avatar { width: 66px; height: 66px; border-radius: 50%; background: var(--grey-avatar); border: 3px solid #d6d6d6; margin-right: 16px; flex: none; }
  .speaker-name { font-size: 24px; white-space: nowrap; }
  .details { position: absolute; left: 535px; top: 918px; color: var(--grey-text); }
  .detail-row { display: flex; align-items: center; font-size: 19px; font-weight: 700; height: 39px; white-space: nowrap; }
  .detail-row svg { width: 24px; height: 24px; margin-right: 8px; flex: none; }
  .venue { display: flex; margin-top: 20px; font-size: 15.5px; line-height: 19px; color: var(--ink); }
  .venue svg { width: 24px; height: 36px; margin-right: 8px; flex: none; }
  .venue-room { margin-top: 19px; }
  .contact { position: absolute; right: 33px; top: 1167px; text-align: right; color: var(--white); }
  .contact-title { font-size: 26px; font-weight: 700; margin-bottom: 6px; }
  .contact-line { display: flex; justify-content: flex-end; align-items: center; font-size: 20px; height: 31px; }
  .contact-line svg { width: 20px; height: 20px; margin-left: 12px; }
  .contact-web { letter-spacing: 3px; }
</style>
</head>
<body>
<article class="flyer">
  <svg class="shapes" viewBox="0 0 940 1330" width="940" height="1330">
    <defs>
      <linearGradient id="panelShade" x1="0" x2="1">
        <stop offset="0" stop-color="#ffffff"/><stop offset="1" stop-color="#ececec"/>
      </linearGradient>
      <linearGradient id="photoTone" x1="0" y1="0" x2="1" y2="1">
        <stop offset="0" stop-color="#2c3e5c"/><stop offset=".5" stop-color="#8da4c4"/><stop offset="1" stop-color="#5a3a2c"/>
      </linearGradient>
    </defs>
    <rect x="0" y="700" width="480" height="630" fill="url(#panelShade)"/>
    <polygon points="940,625 940,790 720,700" fill="#e6e6e6"/>
    <rect x="20" y="50" width="900" height="590" rx="40" fill="url(#photoTone)" role="img" aria-label="Photo of four smiling young adults with backpacks"/>
    <path d="M0,510 C40,570 100,610 170,600 L940,330 L940,625 L220,815 C120,840 40,830 0,800 Z" fill="var(--orange)"/>
    <path d="M190,1330 L780,1145 C850,1122 900,1124 940,1140 L940,1330 Z" fill="var(--orange)"/>
  </svg>

  <div class="brand"><span class="brand-dot"></span><span class="brand-name">MERVAL</span></div>

  <div class="headline">
    <div class="headline-title">MERIVAL 2017</div>
    <div class="headline-sub">Harvest of lanterns conference</div>
  </div>

  <h2 class="theme">YOUR SONS AND DAUGHTERS<br>SHALL PROPHESY</h2>

  <section class="speakers">
    <h3 class="speakers-title">Speakers:</h3>
    <div class="speaker"><span class="speaker-avatar"></span><span class="speaker-name">Prophet Armand Lukeni</span></div>
    <div class="speaker"><span class="speaker-avatar"></span><span class="speaker-name">Bishop Samuel Tshibola</span></div>
    <div class="speaker"><span class="speaker-avatar"></span><span class="speaker-name">Prophet Gabriel Mwamba Ilunga</span></div>
    <div class="speaker"><span class="speaker-avatar"></span><span class="speaker-name">Prophet Rene Kabongo</span></div>
    <div class="speaker"><span class="speaker-avatar"></span><span class="speaker-name">Prophet Joel Mutombo</span></div>
  </section>

  <section class="details">
    <div class="detail-row">
      <svg viewBox="0 0 24 24"><rect x="2" y="4" width="20" height="17" fill="none" stroke="var(--orange)" stroke-width="1.6"/><line x1="2" y1="8" x2="22" y2="8" stroke="var(--orange)" stroke-width="1.6"/><line x1="7" y1="2" x2="7" y2="6" stroke="var(--orange)" stroke-width="1.6"/><line x1="17" y1="2" x2="17" y2="6" stroke="var(--orange)" stroke-width="1.6"/></svg>
      September 1st, 2nd and 3rd 2017
    </div>
    <div class="detail-row">
      <svg viewBox="0 0 24 24"><circle cx="12" cy="12" r="10" fill="none" stroke="var(--orange)" stroke-width="1.8"/><path d="M12 6v6l4 3" fill="none" stroke="var(--orange)" stroke-width="1.8"/></svg>
      Start Time: 6:00PM
    </div>
    <div class="venue">
      <svg viewBox="0 0 24 36"><path d="M12 1C6 1 2 5.5 2 11c0 8 10 23 10 23s10-15 10-23C22 5.5 18 1 12 1z" fill="var(--orange)"/><circle cx="12" cy="11" r="4" fill="#fff"/></svg>
      <div>Harbor View Lodge<br>218 Cedar Lane<br>Millbrook, ME 04999 United States<div class="venue-room">Room: Maple Ballroom</div></div>
    </div>
  </section>

  <section class="contact">
    <h3 class="contact-title">Contact Info:</h3>
    <div class="contact-line">+1 (207) 555 0142
      <svg viewBox="0 0 24 24"><path d="M6 3l4 4-2 3c1 3 3 5 6 6l3-2 4 4-3 3C10 21 3 14 3 6z" fill="none" stroke="#fff" stroke-width="1.8"/></svg></div>
    <div class="contact-line">hello@lanternhouse.org
      <svg viewBox="0 0 24 24"><rect x="2" y="5" width="20" height="14" fill="none" stroke="#fff" stroke-width="1.8"/><path d="M2 5l10 8 10-8" fill="none" stroke="#fff" stroke-width="1.8"/></svg></div>
    <div class="contact-line contact-web">www.lanternhouse.org
      <svg viewBox="0 0 24 24"><circle cx="12" cy="12" r="10" fill="none" stroke="#fff" stroke-width="1.8"/><ellipse cx="12" cy="12" rx="4.5" ry="10" fill="none" stroke="#fff" stroke-width="1.5"/><line x1="2" y1="12" x2="22" y2="12" stroke="#fff" stroke-width="1.5"/></svg></div>
  </section>
</article>
</body>
</html>
```